Wordpress Template Design using existing Logo and Colors

We are wanting a wordpress theme designing for our b2b marketing consultancy business. A comprehesive and elagant design to our current site www.pelvarogroup.com would be good.

Industry/Entity Type

Marketing

Font styles to use
Sans Serif

```html
<!DOCTYPE html>
<html lang="en">
<head>
<meta charset="utf-8">
<title>Pelvaro Group – B2B Data &amp; Marketing</title>
<link rel="stylesheet" href="https://fonts.googleapis.com/css2?family=Montserrat:wght@400;500;600;700&family=Open+Sans:wght@400;600;700&display=swap">
<style>
:root{
  --red:#e4252f;
  --red-dark:#c81d26;
  --navy:#3d4859;
  --ink:#222;
  --text:#666;
  --muted:#999;
  --light:#f1f1f1;
  --footer:#121212;
  --footer-bar:#070707;
  --white:#fff;
  --star:#f2b01e;
}
*{box-sizing:border-box;margin:0;padding:0}
html,body{width:1200px;height:3644px;overflow:hidden}
body{font-family:"Open Sans",Arial,sans-serif;color:var(--text);background:var(--white);position:relative}
h1,h2,h3,h4,.brand,.btn{font-family:"Montserrat",Arial,sans-serif}
a{color:inherit;text-decoration:none}

/* top bar */
.topbar{height:34px;background:var(--navy);color:#dfe3ea;font-size:13px;display:flex;align-items:center;justify-content:space-between;padding:0 100px}
.topbar .contacts span{margin-right:22px}
.topbar .socials{display:flex;gap:10px}
.topbar .socials i{display:block;width:11px;height:11px;background:#dfe3ea;border-radius:2px}

/* header */
.site-header{height:106px;display:flex;align-items:center;padding:0 100px;justify-content:space-between}
.brand{display:flex;align-items:center;gap:10px;font-weight:700;font-size:34px;color:var(--red);letter-spacing:1px}
.brand .mark{width:14px;height:14px;background:var(--navy)}
.main-nav{display:flex;align-items:center;gap:64px;font-family:"Montserrat",sans-serif;font-size:14px;color:#444;text-transform:uppercase}
.main-nav .cta{border:2px solid var(--red);color:var(--red);padding:9px 16px;border-radius:3px}

/* hero */
.hero{position:relative;height:540px;background:linear-gradient(135deg,#6c7683 0%,#b6bcc3 40%,#d7d9dc 60%,#8a8f95 100%);overflow:hidden}
.hero .photo{position:absolute;inset:0}
.hero .banner{position:absolute;left:0;top:190px;width:710px;height:140px;background:rgba(228,37,47,.9);clip-path:polygon(0 0,100% 0,84% 100%,0 100%)}
.hero h1{position:absolute;left:90px;top:212px;color:var(--white);font-size:40px;line-height:52px;font-weight:600}
.hero .arrow{position:absolute;top:250px;width:40px;height:40px}
.hero .arrow.prev{left:20px}.hero .arrow.next{right:20px}
.hero .dots{position:absolute;left:550px;bottom:38px;display:flex;gap:8px}
.hero .dots i{width:12px;height:12px;border-radius:50%;background:rgba(255,255,255,.7)}
.hero .dots i:first-child{background:var(--white)}

/* section heading */
.sec-title{text-align:center;color:var(--ink);font-size:42px;font-weight:600}
.divider{display:flex;justify-content:center;align-items:center;margin:16px 0 0}
.divider::before,.divider::after{content:"";width:110px;height:1px;background:#ccc}
.divider span{width:12px;height:12px;background:var(--red);margin:0 10px}

/* services */
.services{height:622px;padding-top:80px}
.services .intro{width:760px;margin:34px auto 0;text-align:center;font-size:13.5px;line-height:24px}
.svc-grid{width:900px;margin:40px auto 0;display:grid;grid-template-columns:1fr 1fr;row-gap:50px;column-gap:180px}
.svc{position:relative}
.svc h3{font-size:17px;color:var(--ink);font-weight:600;margin-bottom:8px;text-transform:uppercase}
.svc p{font-size:13.5px;line-height:24px}
.svc .more{color:var(--red);font-size:13px;margin-top:8px;display:block}
.svc.left{text-align:right;padding-right:20px}
.svc.right{padding-left:20px}
.svc .icon{position:absolute;top:0;width:104px;height:104px;border-radius:50%;display:flex;align-items:center;justify-content:center}
.svc.left .icon{right:-142px}
.svc.right .icon{left:-142px}
.icon.red{background:var(--red)}
.icon.navy{background:var(--navy)}

/* brochure */
.brochure{height:164px;background:linear-gradient(90deg,#1b3c6e 0%,#26518a 45%,#5f7ea8 75%,#98aac4 100%);color:var(--white);position:relative;padding:34px 0 0 135px}
.brochure h2{font-size:28px;font-weight:600;letter-spacing:1px}
.brochure p{font-size:15px;line-height:25px;margin-top:8px;width:640px}
.brochure .btn{position:absolute;right:135px;top:58px;background:var(--white);color:var(--navy);font-weight:600;font-size:15px;padding:13px 26px;border-radius:3px;text-transform:uppercase}

/* blog */
.blog{height:704px;padding-top:76px;position:relative}
.cards{display:flex;gap:28px;justify-content:center;margin-top:44px}
.card{width:324px;border:1px solid #e6e6e6;background:var(--white);padding:10px 10px 22px}
.card .thumb{height:214px}
.card h4{font-size:17px;color:var(--ink);font-weight:600;margin:28px 0 12px}
.card p{font-size:13.5px;line-height:24px}
.card .meta{font-size:12px;color:var(--red);margin-top:40px}
.slider-arrow{position:absolute;width:44px;height:44px;border-radius:50%;border:1px solid #ccc;top:410px;display:flex;align-items:center;justify-content:center}

/* testimonials */
.testimonials{height:472px;background:var(--light);padding-top:66px;position:relative}
.quotes{display:flex;justify-content:center;gap:60px;margin-top:50px}
.quote{width:310px;display:grid;grid-template-columns:74px 1fr;column-gap:16px}
.quote .avatar{width:72px;height:72px;border-radius:50%;border:3px solid var(--white);background:linear-gradient(#c9b7a6,#8c7b6d)}
.quote blockquote{font-size:13px;line-height:22px;color:var(--muted);font-style:italic}
.quote .who{grid-column:1/3;margin-top:16px;font-size:12px;text-transform:uppercase;color:#444}
.quote .role{grid-column:1/3;font-size:12px;color:var(--text)}
.quote .stars{grid-column:1/3;margin-top:22px;display:flex;gap:4px}

/* contact */
.contact{height:603px;background:linear-gradient(180deg,var(--red) 0%,#e93a40 100%);padding-top:80px}
.contact .sec-title{color:var(--white)}
.contact .divider::before,.contact .divider::after{background:rgba(255,255,255,.5)}
.contact .divider span{background:var(--white)}
.form{width:910px;margin:44px auto 0;display:grid;grid-template-columns:1fr 1fr;gap:16px 14px}
.field{height:46px;background:var(--white);padding:14px 16px;font-size:13px;color:var(--muted)}
.field.message{grid-column:1/3;height:114px}
.form .submit{grid-column:1/3;justify-self:center;width:380px;height:46px;background:var(--navy);color:var(--white);font-weight:600;font-size:15px;display:flex;align-items:center;justify-content:center;text-transform:uppercase;margin-top:6px;letter-spacing:.5px}

/* footer */
.site-footer{height:345px;background:var(--footer);color:#d0d0d0;display:grid;grid-template-columns:335px 270px 270px 1fr;padding:50px 0 0 100px}
.site-footer .brand{font-size:30px;margin-top:20px}
.site-footer h4{color:var(--white);font-size:19px;font-weight:600;margin-bottom:22px;text-decoration:underline;text-underline-offset:6px}
.follow h4{margin-top:48px;margin-bottom:14px}
.social{display:flex;gap:10px}
.social i{width:30px;height:30px;border-radius:50%}
.info li{list-style:none;display:flex;gap:14px;font-size:12.5px;line-height:19px;margin-bottom:12px}
.info svg{flex:none;margin-top:3px}
.links li{list-style:none;font-size:12.5px;line-height:23px}
.copyright{position:absolute;left:0;top:3590px;width:1200px;height:54px;background:var(--footer-bar);color:#ccc;font-size:12.5px;display:flex;align-items:center;justify-content:center}
</style>
</head>
<body>

<div class="topbar">
  <div class="contacts"><span>&#9742; Call us : +1 (555) 014-2290</span><span>&#9993; Email us : contact.sg@pelvarogroup.com</span></div>
  <div class="socials"><i></i><i></i><i></i><i></i><i></i></div>
</div>

<header class="site-header">
  <a class="brand" href="#"><span>PELVARO</span><span class="mark"></span></a>
  <nav class="main-nav">
    <a href="#">Target Marketing</a>
    <a href="#">Data Management</a>
    <a href="#">About</a>
    <a class="cta" href="#">Get an Appointment</a>
  </nav>
</header>

<section class="hero">
  <div class="photo" role="img" aria-label="Business person at a desk with a laptop, aiming a dart at a dartboard"></div>
  <div class="banner"></div>
  <h1>Inbound &amp; Outbound<br>Call Centres</h1>
  <svg class="arrow prev" viewBox="0 0 40 40"><path d="M25 8 13 20l12 12" fill="none" stroke="#fff" stroke-width="3"/></svg>
  <svg class="arrow next" viewBox="0 0 40 40"><path d="M15 8l12 12-12 12" fill="none" stroke="#fff" stroke-width="3"/></svg>
  <div class="dots"><i></i><i></i><i></i><i></i></div>
</section>

<section class="services">
  <h2 class="sec-title">Our Services</h2>
  <div class="divider"><span></span></div>
  <p class="intro">We are a B2B Data, Analytics and Marketing Consulting Company specialized in harnessing the power of potential data to strengthen connections between decisions makers, companies and products. We focus on solutions engineered to solve distinct challenges in the data, direct marketing, and analytics space.</p>
  <div class="svc-grid">
    <div class="svc left">
      <h3>B2B Database</h3>
      <p>Get access to Asia's leading market &amp; business intelligence database over 1,500,000 organizations and</p>
      <a class="more" href="#">Read More &rsaquo;</a>
      <div class="icon red"><svg width="46" height="50" viewBox="0 0 46 50" fill="#fff"><ellipse cx="23" cy="8" rx="20" ry="7"/><path d="M3 14c0 4 9 7 20 7s20-3 20-7v8c0 4-9 7-20 7S3 26 3 22z"/><path d="M3 28c0 4 9 7 20 7s20-3 20-7v8c0 4-9 7-20 7S3 40 3 36z"/></svg></div>
    </div>
    <div class="svc right">
      <h3>Target Marketing</h3>
      <p>We develop tailored marketing solutions based on your specific objectives, audience and budget to</p>
      <a class="more" href="#">Read More &rsaquo;</a>
      <div class="icon navy"><svg width="54" height="54" viewBox="0 0 54 54" fill="none" stroke="#fff" stroke-width="4"><circle cx="27" cy="27" r="23"/><circle cx="27" cy="27" r="14"/><circle cx="27" cy="27" r="5" fill="#fff"/></svg></div>
    </div>
    <div class="svc left">
      <h3>Call Centre</h3>
      <p>When your business requires instantaneous and cost effective contact center, we are here to provide the</p>
      <a class="more" href="#">Read More &rsaquo;</a>
      <div class="icon navy"><svg width="50" height="48" viewBox="0 0 50 48" fill="none" stroke="#fff" stroke-width="4"><path d="M7 30V24a18 18 0 0 1 36 0v6"/><rect x="4" y="28" width="9" height="15" rx="3" fill="#fff"/><rect x="37" y="28" width="9" height="15" rx="3" fill="#fff"/></svg></div>
    </div>
    <div class="svc right">
      <h3>Data Management</h3>
      <p>We analyze your data and report on effective strategies for turning the data into a profitable resource.</p>
      <a class="more" href="#">Read More &rsaquo;</a>
      <div class="icon red"><svg width="56" height="44" viewBox="0 0 56 44" fill="#fff"><circle cx="28" cy="11" r="8"/><path d="M14 42c0-10 6-16 14-16s14 6 14 16z"/><circle cx="10" cy="16" r="6"/><path d="M0 40c0-8 4-12 10-12 3 0 5 1 6 2-3 3-4 6-4 10z"/><circle cx="46" cy="16" r="6"/><path d="M56 40c0-8-4-12-10-12-3 0-5 1-6 2 3 3 4 6 4 10z"/></svg></div>
    </div>
  </div>
</section>

<section class="brochure" role="img" aria-label="City skyline at dusk behind the brochure banner">
  <h2>CORPORATE BROCHURE</h2>
  <p>Learn our leading target marketing and intelligent data management solutions to attain new customers for your niche products and services.</p>
  <a class="btn" href="#">&#10515; Download Now</a>
</section>

<section class="blog">
  <h2 class="sec-title">Our Blog posts</h2>
  <div class="divider"><span></span></div>
  <div class="slider-arrow" style="left:40px"><svg width="14" height="14" viewBox="0 0 14 14"><path d="M9 2 4 7l5 5" fill="none" stroke="#bbb" stroke-width="2"/></svg></div>
  <div class="slider-arrow" style="right:40px"><svg width="14" height="14" viewBox="0 0 14 14"><path d="M5 2l5 5-5 5" fill="none" stroke="#bbb" stroke-width="2"/></svg></div>
  <div class="cards">
    <article class="card">
      <div class="thumb" role="img" aria-label="Laptop on a desk showing a marketing strategy chart" style="background:linear-gradient(135deg,#c7c2ba,#8d8a86)"></div>
      <h4>Sed ut perspiciatis unde omnis</h4>
      <p>But I must explain to you how all this mistaken idea of denouncing pasure and praisingleasure and presing pain was born mplete accoun.</p>
      <div class="meta">&#9679; By admin &nbsp;|&nbsp; Nov 17 2017 &nbsp;|&nbsp; comments</div>
    </article>
    <article class="card">
      <div class="thumb" role="img" aria-label="Green chalkboard with target-your-customers lettering" style="background:linear-gradient(135deg,#3f7a45,#2a5a30)"></div>
      <h4>Sed ut perspiciatis unde omnis</h4>
      <p>But I must explain to you how all this mistaken idea of denouncing pasure and praisingleasure and presing pain was born mplete accoun.</p>
      <div class="meta">&#9679; By admin &nbsp;|&nbsp; Nov 17 2017 &nbsp;|&nbsp; comments</div>
    </article>
    <article class="card">
      <div class="thumb" role="img" aria-label="Hand touching a glowing target in a network of icons" style="background:radial-gradient(circle at 50% 45%,#3f78b8,#0d2748)"></div>
      <h4>Sed ut perspiciatis unde omnis</h4>
      <p>But I must explain to you how all this mistaken idea of denouncing pasure and praisingleasure and presing pain was born mplete accoun.</p>
      <div class="meta">&#9679; By admin &nbsp;|&nbsp; Nov 17 2017 &nbsp;|&nbsp; comments</div>
    </article>
  </div>
</section>

<section class="testimonials">
  <h2 class="sec-title">Client Testimonials</h2>
  <div class="divider"><span></span></div>
  <div class="slider-arrow" style="left:24px;top:222px"><svg width="14" height="14" viewBox="0 0 14 14"><path d="M9 2 4 7l5 5" fill="none" stroke="#bbb" stroke-width="2"/></svg></div>
  <div class="slider-arrow" style="right:24px;top:222px"><svg width="14" height="14" viewBox="0 0 14 14"><path d="M5 2l5 5-5 5" fill="none" stroke="#bbb" stroke-width="2"/></svg></div>
  <div class="quotes">
    <div class="quote">
      <div class="avatar" role="img" aria-label="Client portrait"></div>
      <blockquote>&ldquo; At vero eos et accusamus et iusto odio dignissimos ducimus qui blanditiisraesent sum voluptat atqu.</blockquote>
      <div class="who">Dana Whitfield</div>
      <div class="role">Financial Services Professional</div>
      <div class="stars"><svg width="96" height="18" viewBox="0 0 96 18"><g fill="#f2b01e"><path id="s" d="M9 1l2.4 5.2 5.6.6-4.2 3.8 1.2 5.6L9 13.4 4 16.2l1.2-5.6L1 6.8l5.6-.6z"/><use href="#s" x="19"/><use href="#s" x="38"/><use href="#s" x="57"/></g><use href="#s" x="76" fill="none" stroke="#f2b01e"/></svg></div>
    </div>
    <div class="quote">
      <div class="avatar" role="img" aria-label="Client portrait" style="background:linear-gradient(#bfbfbf,#6f6f6f)"></div>
      <blockquote>&ldquo; At vero eos et accusamus et iusto odio dignissimos ducimus qui blanditiisraesent sum voluptat atqu.</blockquote>
      <div class="who">Marcus T. Ellison</div>
      <div class="role">National Urban Fellow at the Housing</div>
      <div class="stars"><svg width="96" height="18" viewBox="0 0 96 18"><g fill="#f2b01e"><use href="#s"/><use href="#s" x="19"/><use href="#s" x="38"/><use href="#s" x="57"/><use href="#s" x="76"/></g></svg></div>
    </div>
    <div class="quote">
      <div class="avatar" role="img" aria-label="Client portrait" style="background:linear-gradient(#d6c6b5,#9a8878)"></div>
      <blockquote>&ldquo; At vero eos et accusamus et iusto odio dignissimos ducimus qui blanditiisraesent sum voluptat atqu.</blockquote>
      <div class="who">Rita Okafor</div>
      <div class="role">Creative Strategist | Entrepreneur &amp; Upcoming</div>
      <div class="stars"><svg width="96" height="18" viewBox="0 0 96 18"><g fill="#f2b01e"><use href="#s"/><use href="#s" x="19"/><use href="#s" x="38"/><use href="#s" x="57"/></g><use href="#s" x="76" fill="none" stroke="#f2b01e"/></svg></div>
    </div>
  </div>
</section>

<section class="contact">
  <h2 class="sec-title">Contact Form</h2>
  <div class="divider"><span></span></div>
  <div class="form">
    <div class="field">Name</div>
    <div class="field">Email</div>
    <div class="field">Phone</div>
    <div class="field">Address</div>
    <div class="field message">Message</div>
    <div class="submit">Submit Message</div>
  </div>
</section>

<footer class="site-footer">
  <div>
    <div class="brand"><span>PELVARO</span><span class="mark" style="background:#fff"></span></div>
    <div class="follow">
      <h4>Follow us</h4>
      <div class="social"><i style="background:#3b5998"></i><i style="background:#1da1f2"></i><i style="background:#dd4b39"></i><i style="background:#555"></i><i style="background:#e52d27"></i><i style="background:#0077b5"></i></div>
    </div>
  </div>
  <div>
    <h4>Global HQ</h4>
    <ul class="info">
      <li><svg width="10" height="14" viewBox="0 0 10 14"><path d="M5 0a5 5 0 0 1 5 5c0 4-5 9-5 9S0 9 0 5a5 5 0 0 1 5-5z" fill="#fff"/></svg><span>2140 Harbor Crest Way, Suite 210,<br>Oceanview CA 90410, USA</span></li>
      <li><svg width="12" height="12" viewBox="0 0 12 12"><path d="M2 0l3 3-2 2c1 2 2 3 4 4l2-2 3 3-2 2C5 12 0 7 0 2z" fill="#fff"/></svg><span>+1 (555) 014-2290</span></li>
      <li><svg width="12" height="12" viewBox="0 0 12 12"><circle cx="6" cy="6" r="6" fill="#fff"/></svg><span>contact@pelvarogroup.com</span></li>
      <li><svg width="12" height="12" viewBox="0 0 12 12"><circle cx="6" cy="6" r="6" fill="#fff"/></svg><span>www.pelvarogroup.com</span></li>
      <li><svg width="12" height="12" viewBox="0 0 12 12"><circle cx="6" cy="6" r="5" fill="none" stroke="#fff" stroke-width="2"/></svg><span>Monday - Friday : 9AM - 6PM</span></li>
    </ul>
  </div>
  <div>
    <h4>Regional HQ</h4>
    <ul class="info">
      <li><svg width="10" height="14" viewBox="0 0 10 14"><path d="M5 0a5 5 0 0 1 5 5c0 4-5 9-5 9S0 9 0 5a5 5 0 0 1 5-5z" fill="#fff"/></svg><span>18 Merlin Park Road, #04-07 Keystone<br>Hub, Singapore 419920</span></li>
      <li><svg width="12" height="12" viewBox="0 0 12 12"><path d="M2 0l3 3-2 2c1 2 2 3 4 4l2-2 3 3-2 2C5 12 0 7 0 2z" fill="#fff"/></svg><span>+65 6100 4821</span></li>
      <li><svg width="12" height="12" viewBox="0 0 12 12"><circle cx="6" cy="6" r="6" fill="#fff"/></svg><span>contact.sg@pelvarogroup.com</span></li>
      <li><svg width="12" height="12" viewBox="0 0 12 12"><circle cx="6" cy="6" r="6" fill="#fff"/></svg><span>www.pelvarogroup.com</span></li>
      <li><svg width="12" height="12" viewBox="0 0 12 12"><circle cx="6" cy="6" r="5" fill="none" stroke="#fff" stroke-width="2"/></svg><span>Monday - Friday : 9AM - 6PM</span></li>
    </ul>
  </div>
  <div>
    <h4>Quick Links</h4>
    <ul class="links">
      <li>B2B Database</li><li>Call Centre</li><li>Demand Generation</li><li>Lead Generation</li><li>Data Management</li><li>Marketing Automation</li><li>Data Append</li><li>Event Management</li><li>Contact Us</li>
    </ul>
  </div>
</footer>
<div class="copyright">&copy; copyright 2018 Pelvaro Group. All Rights Reserved &nbsp;|&nbsp; Privacy policy &nbsp;|&nbsp; Terms and use</div>

</body>
</html>
```